New look and feel for investment website

Hi

Our website needs a crisp and professional look and feel applying to it. Here’s the address: http://www.brightplinth.co.uk. Since posting the brief yesterday (Tuesday, 16 August), we've reduced the amount of content on the home page, which should make life a little easier for you. We will come back later today, with some points of reference in terms of sites we like the look of. (See below)

17 August, 1.20pm GMT. OK, comments generally on the designs submitted so far. Please keep in mind that images of graphs, piles of coins, paper money and pretty females are not what is required. Better to think in terms of abstract imagery instead. Ratios? Circles? Relationships? Patterns? Not money,sex,graphs etc. Hope that helps.

For guidance on look and feel, please refer to these sites, which we like:

http://www.morvelle.co.uk/
http://www.qz.com/
https://www.harrowfieldtamsin.com
https://www.pirelconcerns.com
https://www.kvantule.com
Updates

Here's the Tall Beacons logo created in AI CS5.

Our market is professional financial advisers and relatively sophisticated private investors. The look and feel therefore should be slick and sophisticated - not 'lively' and lightweight, more like a banking site. Please read the brief again where we've added a list of websites that we really like the look of to get a better feel for what we're looking for. Thanks once again, we appreciate the work you're putting in.

It's essential that all the elements that are on the current home page be included on all new designs. 

We use a device in our e-mails which you may wish to incorporate in your design.

Target Market(s)

Professional financial advisers. People who know about investment and money.

Industry/Entity Type

Investment

Requirements
Should not have
• Graphs or people.

```html
<!DOCTYPE html>
<html lang="en">
<head>
<meta charset="utf-8">
<title>Tall Beacons — Home</title>
<link href="https://fonts.googleapis.com/css2?family=Roboto+Condensed:wght@700&family=PT+Sans:wght@400;700&family=Arimo:wght@400;700&display=swap" rel="stylesheet">
<style>
:root{
  --red:#e2483b;
  --red-dark:#c93a2e;
  --ink:#333333;
  --grey-text:#555555;
  --logo-grey:#6a6a6a;
  --accent-orange:#f5a623;
  --bg-light:#f4f4f4;
  --bg-mid:#d6d6d6;
  --white:#ffffff;
  --tone-a:#e9e9e9;
  --tone-b:#bdbdbd;
}
*{margin:0;padding:0;box-sizing:border-box}
html,body{width:1055px;height:1200px;overflow:hidden;background:var(--white)}
body{position:relative;font-family:"PT Sans",sans-serif;color:var(--ink)}
.abs{position:absolute}

/* ---------- Wide header view ---------- */
.view-wide{left:0;top:0;width:1055px;height:656px;overflow:hidden;
  background:radial-gradient(ellipse 70% 75% at 35% 45%,var(--white) 0%,var(--bg-light) 40%,var(--bg-mid) 100%)}
.brand{font-family:"PT Sans",sans-serif;font-weight:400;color:var(--logo-grey);display:flex;align-items:center;gap:8px;white-space:nowrap}
.brand-dot{display:inline-block;border-radius:50%;background:var(--accent-orange)}
.brand--header{left:121px;top:30px;font-size:48px;letter-spacing:-1px}
.brand--header .brand-dot{width:11px;height:11px}
.main-nav{left:488px;top:0;display:flex;height:84px;font-size:18px;color:var(--ink)}
.main-nav a{color:inherit;text-decoration:none;display:block;padding-top:50px;white-space:nowrap}
.main-nav .is-active{background:var(--red);color:var(--white);width:97px;text-align:center}
.main-nav .n-login{margin-left:26px}
.main-nav .n-register{margin-left:28px}
.main-nav .n-contact{margin-left:44px}
.main-nav .n-terms{margin-left:37px}

/* abstract imagery area: soft tonal field, no figures */
.abstract-field{background:radial-gradient(ellipse 60% 55% at 50% 45%,var(--tone-a) 0%,rgba(189,189,189,.35) 60%,rgba(214,214,214,0) 100%)}

.headline{font-family:"Roboto Condensed",sans-serif;font-weight:700;color:var(--red);letter-spacing:-1px;white-space:nowrap}
.subhead{font-family:"Roboto Condensed",sans-serif;font-weight:700;text-transform:uppercase;color:var(--ink);white-space:nowrap}
.aside-note{font-family:"PT Sans",sans-serif;color:var(--ink);white-space:nowrap}
.ratio-mark{overflow:visible}

.feature-band{display:flex;background:var(--red);color:var(--white)}
.feature{position:relative;border-right:1px solid var(--red-dark);flex:none}
.feature:last-child{border-right:none}
.feature svg{position:absolute}
.feature h3{position:absolute;font-family:"PT Sans",sans-serif;font-weight:400;white-space:nowrap}
.feature p{position:absolute;font-family:"Arimo",sans-serif;line-height:1.2}

/* wide sizes */
.view-wide .headline{left:132px;top:226px;font-size:47px}
.view-wide .subhead{left:137px;top:292px;font-size:20.5px;line-height:31px}
.view-wide .aside-note{left:140px;top:370px;font-size:15.5px;line-height:26px}
.view-wide .ratio-mark{left:607px;top:369px;width:89px;height:88px}
.view-wide .brand--inline{left:564px;top:459px;font-size:40px}
.view-wide .brand--inline .brand-dot{width:9px;height:9px}
.view-wide .abstract-field{left:800px;top:100px;width:300px;height:437px}
.view-wide .feature-band{left:80px;top:537px;width:1000px;height:119px}
.view-wide .feature{width:395px}
.view-wide .feature:nth-child(3){width:210px}
.view-wide .feature svg{left:28px;top:24px;width:70px;height:72px}
.view-wide .feature h3{left:119px;top:13px;font-size:24px}
.view-wide .feature p{left:120px;top:52px;font-size:14px;width:220px}

/* ---------- Full page view ---------- */
.view-full{left:0;top:656px;width:1055px;height:544px;overflow:hidden;
  background:radial-gradient(ellipse 60% 70% at 40% 35%,var(--white) 0%,var(--bg-light) 45%,var(--bg-mid) 100%)}
.view-full .headline{left:84px;top:112px;font-size:37px}
.view-full .subhead{left:88px;top:166px;font-size:17px;line-height:25px}
.view-full .aside-note{left:90px;top:227px;font-size:12.5px;line-height:20px}
.view-full .ratio-mark{left:472px;top:223px;width:73px;height:73px}
.view-full .brand--inline{left:436px;top:300px;font-size:32px}
.view-full .brand--inline .brand-dot{width:8px;height:8px}
.view-full .abstract-field{left:640px;top:10px;width:340px;height:353px}
.view-full .feature-band{left:41px;top:363px;width:957px;height:98px}
.view-full .feature{width:322px}
.view-full .feature:nth-child(2){width:305px}
.view-full .feature:nth-child(3){width:330px}
.view-full .feature svg{left:22px;top:20px;width:58px;height:60px}
.view-full .feature h3{left:97px;top:10px;font-size:20px}
.view-full .feature p{left:98px;top:44px;font-size:11px;width:172px}

.content{left:41px;top:461px;width:957px;height:83px;background:var(--white);display:flex}
.sidebar{width:256px;flex:none;background:linear-gradient(90deg,#fafafa,#eeeeee);padding-top:28px}
.sidebar li{list-style:none;display:flex;align-items:center;gap:12px;padding-left:22px;font-family:"Arimo",sans-serif;font-size:12.5px;color:var(--grey-text);height:26px;border-bottom:1px solid #e3e3e3;width:240px;white-space:nowrap}
.sidebar svg{width:12px;height:12px;flex:none}
.article{padding:27px 0 0 25px}
.article h2{font-family:"Arimo",sans-serif;font-weight:700;font-size:17px;color:#555;margin-bottom:12px}
.article p{font-family:"Arimo",sans-serif;font-size:12px;color:#777;white-space:nowrap}
</style>
</head>
<body>

<svg width="0" height="0" class="abs" aria-hidden="true">
  <defs>
    <symbol id="icon-target" viewBox="0 0 70 72">
      <g fill="none" stroke="#fff" stroke-width="3">
        <circle cx="35" cy="36" r="30"/>
        <circle cx="35" cy="36" r="19"/>
      </g>
      <circle cx="35" cy="36" r="8" fill="#fff"/>
    </symbol>
    <symbol id="icon-document" viewBox="0 0 70 72">
      <g fill="none" stroke="#fff" stroke-width="3.5" stroke-linejoin="round">
        <path d="M14 4H44L58 18V68H14Z"/>
        <path d="M44 4V18H58"/>
        <path d="M24 32H48M24 43H48M24 54H40"/>
      </g>
    </symbol>
    <symbol id="icon-screen" viewBox="0 0 70 72">
      <g fill="none" stroke="#fff" stroke-width="4">
        <rect x="4" y="8" width="62" height="40" rx="4"/>
        <rect x="4" y="54" width="62" height="10" rx="4"/>
      </g>
      <path d="M18 18L34 26L27 28L33 36L29 38L23 30L18 35Z" fill="#fff"/>
    </symbol>
    <symbol id="ratio-circles" viewBox="0 0 90 90">
      <circle cx="34" cy="50" r="30" fill="var(--red)" opacity=".85"/>
      <circle cx="62" cy="32" r="22" fill="var(--accent-orange)" opacity=".85"/>
    </symbol>
  </defs>
</svg>

<!-- Wide header view -->
<section class="abs view-wide">
  <div class="abs abstract-field" role="img" aria-label="Soft abstract tonal field"></div>
  <div class="abs brand brand--header">Tall Beacons<span class="brand-dot"></span></div>
  <nav class="abs main-nav">
    <a class="is-active" href="#">Home</a>
    <a class="n-login" href="#">Login</a>
    <a class="n-register" href="#">Register for free</a>
    <a class="n-contact" href="#">Contact us</a>
    <a class="n-terms" href="#">Terms &amp;</a>
  </nav>
  <h1 class="abs headline">A POTENTIAL RETURN OF 23.57 %</h1>
  <p class="abs subhead">A year from America’s biggest businesses with the emphasis<br>firmly on capital preservation.</p>
  <p class="abs aside-note">(OK: we know you've yet to learn to love it, so that's why &nbsp;you can use<br>our service free of charge for six months!)</p>
  <svg class="abs ratio-mark" aria-hidden="true"><use href="#ratio-circles"/></svg>
  <div class="abs brand brand--inline">Tall Beacons<span class="brand-dot"></span></div>
  <div class="abs feature-band">
    <div class="feature"><svg><use href="#icon-target"/></svg><h3>Our service and Results</h3><p>To use our service free of charge for six months, please register here.</p></div>
    <div class="feature"><svg><use href="#icon-document"/></svg><h3>About value investing</h3><p>To use our service free of charge for six months, please register here.</p></div>
    <div class="feature"><svg><use href="#icon-screen"/></svg><h3>Register for free</h3><p>To use our service free of charge for six months, please register here.</p></div>
  </div>
</section>

<!-- Full page view -->
<section class="abs view-full">
  <div class="abs abstract-field" role="img" aria-label="Soft abstract tonal field"></div>
  <h1 class="abs headline">A POTENTIAL RETURN OF 23.57 %</h1>
  <p class="abs subhead">A year from America’s biggest businesses with the emphasis<br>firmly on capital preservation.</p>
  <p class="abs aside-note">(OK: we know you've yet to learn to love it, so that's why &nbsp;you can use<br>our service free of charge for six months!)</p>
  <svg class="abs ratio-mark" aria-hidden="true"><use href="#ratio-circles"/></svg>
  <div class="abs brand brand--inline">Tall Beacons<span class="brand-dot"></span></div>
  <div class="abs feature-band">
    <div class="feature"><svg><use href="#icon-target"/></svg><h3>Our service and Results</h3><p>To use our service free of charge for six months, please register here.</p></div>
    <div class="feature"><svg><use href="#icon-document"/></svg><h3>About value investing</h3><p>To use our service free of charge for six months, please register here.</p></div>
    <div class="feature"><svg><use href="#icon-screen"/></svg><h3>Register for free</h3><p>To use our service free of charge for six months, please register here.</p></div>
  </div>
  <div class="abs content">
    <ul class="sidebar">
      <li><svg viewBox="0 0 12 12"><rect width="12" height="12" fill="#e4e4e4"/><path d="M3 6H9M6 3L9 6L6 9" stroke="#444" stroke-width="1.4" fill="none"/></svg>Two Minute Guide</li>
      <li><svg viewBox="0 0 12 12"><rect width="12" height="12" fill="#e4e4e4"/><path d="M3 6H9M6 3L9 6L6 9" stroke="#444" stroke-width="1.4" fill="none"/></svg>Current &amp; year to date performance</li>
    </ul>
    <div class="article">
      <h2>BEFORE GETTING INTO THE DETAIL...</h2>
      <p>You may well be thinking that Tall Beacons is just another one of those banal share recommendation sites sprinkled with</p>
    </div>
  </div>
</section>

</body>
</html>
```